Specialist Recruitment Process Outsourcing (RPO) company needs a modern, sleek website

We need a website which showcases our service offering, describes our onshore and offshore options. Our service is basically building teams of recruiters who become the outsourced (but in-house) recruiter for that specific client. Our logo colours include a light, bright green and a dark/midnight blue. This company will be targeting companies who need help with recruitment in technology, finance, engineering and other white collar industries. We are looking for a look and feeling that communicates cutting edge technology with a bright, energetic appeal. I will include some logo design files to work with.

Target Market(s)

Businesses: start ups who need to grow their staff, SMEs with regular recruitment needs, and larger businesses

Industry/Entity Type

Recruitment

Coding

Coded - Design and coding required

Number of Pages Required

4 page

Font styles to use
Sans Serif

Requirements
Must have
• Landing page should be highly visual, either with dynamic image or scrolling stills accompanies by our core service offering, values, and benefits.

A Services page will allows more detail about what we do, with a call to action.

A User Stories page will showcase some examples of how our services will help certain types of businesses.

Onshore/Offshore page will breakdown the benefits of both approaches and how combinations can work well.

Should fit the colour theming of our logo (files uploaded).

Nice to have
• Imagery can be both around business and people. We are looking for more of a "startup" feel than a corporate-y feel.

```html
<!DOCTYPE html>
<html lang="en">
<head>
<meta charset="UTF-8">
<title>Crewline — Recruitment Process Outsourcing</title>
<link rel="stylesheet" href="https://fonts.googleapis.com/css2?family=Poppins:wght@400;500;600;700&family=Roboto:ital,wght@0,400;0,500;0,700;1,400&display=swap">
<style>
:root{
  --green:#0be597;
  --green-deep:#05cf86;
  --green-bright:#14f2a2;
  --navy:#121330;
  --navy-2:#1b1f45;
  --ink:#111;
  --muted:#666;
  --light:#f2f2f2;
  --white:#fff;
}
*{box-sizing:border-box;margin:0;padding:0}
html,body{width:1200px;height:4286px;overflow:hidden}
body{position:relative;font-family:'Roboto',sans-serif;color:var(--ink);background:var(--white)}

/* nav + hero */
.hero{position:absolute;left:0;top:0;width:1200px;height:603px;background:linear-gradient(90deg,#f4f5f5 0%,#eceeee 40%,#c9ccd0 60%,#9ea6ad 100%)}
.hero-photo{position:absolute;left:470px;top:0;width:730px;height:603px;background:linear-gradient(90deg,rgba(240,241,241,0) 0%,rgba(180,170,165,.55) 40%,rgba(120,110,105,.6) 70%,rgba(200,205,210,.5) 100%)}
.brand{position:absolute;display:flex;align-items:center;gap:8px;font-family:'Poppins',sans-serif;font-weight:600;letter-spacing:2px;color:var(--green)}
.brand .dot{width:14px;height:14px;border-radius:50%;background:var(--green)}
.nav{position:absolute;left:328px;top:38px;display:flex;font-size:14px;font-family:'Roboto',sans-serif;color:#222}
.nav span{white-space:nowrap}
.nav .sep{margin:0 14px}
.nav .active{color:var(--green)}
.hero-title{position:absolute;left:113px;top:188px;font-family:'Poppins',sans-serif;font-weight:700;color:var(--navy)}
.hero-title .big{font-size:58px;line-height:64px;display:block}
.hero-title .line{font-size:36px;line-height:51px;display:block}
.hero-title .g{color:var(--green)}
.btn{position:absolute;display:flex;align-items:center;justify-content:center;border-radius:22px;font-weight:700;font-size:16px;font-family:'Roboto',sans-serif}
.btn-green{background:var(--green);color:#fff}
.btn-dark{background:var(--navy);color:#fff}
.hero-arrow{position:absolute;top:282px;width:34px;height:34px;border:1.5px solid rgba(160,165,170,.8);border-radius:50%}
.dots{position:absolute;left:500px;top:573px;display:flex;gap:4px}
.dots i{display:block;width:46px;height:3px;background:rgba(255,255,255,.8)}
.dots i.on{background:var(--green)}

/* services */
.services{position:absolute;left:0;top:603px;width:1200px;height:582px;background:var(--light)}
.sec-title{position:absolute;left:0;width:1200px;text-align:center;font-family:'Poppins',sans-serif;font-weight:700;color:var(--navy)}
.sec-sub{position:absolute;left:250px;width:700px;text-align:center;font-size:13.5px;font-weight:500;line-height:27px}
.svc{position:absolute;top:205px;width:340px;text-align:center}
.svc svg{display:block;margin:0 auto}
.svc h3{font-family:'Poppins',sans-serif;font-size:25px;line-height:30px;font-weight:700;color:var(--navy);margin-top:10px}
.svc p{font-size:12.5px;line-height:25.5px;color:#555;margin:14px auto 0;width:305px}
.divider{position:absolute;top:221px;width:2px;height:263px;background:#9a9a9a}
.chev{position:absolute;top:340px}

/* newsletter */
.newsletter{position:absolute;left:0;top:1185px;width:1200px;height:175px;background:linear-gradient(90deg,var(--green-deep),#10e69a)}
.newsletter h2{position:absolute;left:112px;top:66px;font-family:'Poppins',sans-serif;font-size:33px;font-weight:700;color:#fff}
.email{position:absolute;left:679px;top:60px;width:408px;height:56px;border:1px solid #fff;color:#fff;font-size:16px;padding:18px 0 0 22px;font-weight:500}
.email-btn{position:absolute;right:-1px;top:-1px;width:71px;height:56px;background:var(--navy)}

/* value */
.value{position:absolute;left:0;top:1360px;width:1200px;height:610px;background:#ebebeb}
.value-photo{position:absolute;left:700px;top:0;width:500px;height:610px;background:radial-gradient(ellipse at 55% 50%,#8a7e72 0%,#b9b6b1 45%,#e4e4e4 85%)}
.value h2{position:absolute;left:110px;top:78px;font-family:'Poppins',sans-serif;font-size:42px;font-weight:700;color:var(--navy)}
.value .lead{position:absolute;left:112px;top:141px;font-size:18.5px;line-height:30px;color:#222;width:470px}
.vbox{position:absolute;top:233px;width:303px;height:294px;padding:45px 24px 0}
.vbox h3{font-family:'Poppins',sans-serif;font-size:24.5px;line-height:34px;font-weight:600}
.vbox p{font-size:12.8px;line-height:28px;margin-top:14px}
.vbox.dark{left:112px;background:var(--navy);color:#fff}
.vbox.bright{left:415px;background:var(--green-bright);color:#fff;width:305px}

/* stories */
.stories{position:absolute;left:0;top:1970px;width:1200px;height:579px;background:linear-gradient(135deg,#06d98c 0%,#12ec9e 50%,#05d38a 100%)}
.card{position:absolute;top:206px;width:305px;height:290px;background:#fff;border-bottom:9px solid var(--navy);padding:30px 24px 0}
.card .stars{display:flex;gap:2px}
.card .badge{position:absolute;right:24px;top:28px;width:28px;height:28px;border-radius:50%;border:3px solid #c9c9c9}
.card p{font-style:italic;font-size:16px;line-height:28.5px;color:#333;text-align:justify;margin-top:26px}
.card .who{font-weight:500;font-size:18px;margin-top:18px;color:#111}

/* leader */
.leader{position:absolute;left:0;top:2549px;width:1200px;height:571px;background:linear-gradient(135deg,#1e2348 0%,#151837 55%,#1c2146 100%)}
.avatar{position:absolute;left:112px;top:102px;width:102px;height:102px;border-radius:50%;border:3px solid var(--green);background:radial-gradient(circle at 50% 45%,#c8c2bc,#6d7178)}
.leader .name{position:absolute;left:235px;top:114px;font-family:'Poppins',sans-serif;font-size:35px;font-weight:700;color:#fff}
.leader .name span{color:var(--green)}
.leader .role{position:absolute;left:236px;top:165px;font-size:12.5px;color:#fff;font-weight:500}
.leader .bio{position:absolute;left:111px;top:226px;width:460px;font-size:13.5px;line-height:28.3px;color:#fff}
.socials{position:absolute;display:flex;gap:8px}
.socials i{display:block;border:1.5px solid #fff;border-radius:50%}
.vline{position:absolute;left:600px;top:85px;width:1.5px;height:406px;background:rgba(255,255,255,.7)}
.stat{position:absolute;left:642px;width:108px;height:108px;border:2px solid #fff;border-radius:50%;display:flex;align-items:center;justify-content:center;font-family:'Poppins',sans-serif;font-weight:600;font-size:29px;color:var(--green)}
.stat-t{position:absolute;left:771px;font-family:'Poppins',sans-serif;font-size:24px;font-weight:500;color:#fff}
.stat-p{position:absolute;left:771px;width:330px;font-size:13.5px;line-height:26px;color:#fff}

/* news */
.news{position:absolute;left:0;top:3120px;width:1200px;height:632px;background:#fff}
.ncard{position:absolute;top:157px;width:310px;height:392px;background:#fff;box-shadow:0 0 8px rgba(0,0,0,.12)}
.nimg{height:196px}
.ncard h4{font-family:'Roboto',sans-serif;font-weight:700;font-size:17px;line-height:28px;margin:18px 10px 0;color:#111}
.ncard p{font-size:12.5px;line-height:25.5px;color:#777;margin:8px 10px 0}
.ncard .more{font-size:15px;font-weight:500;margin:10px 10px 0;color:#111}

/* contact */
.contact{position:absolute;left:0;top:3752px;width:1200px;height:534px;background:radial-gradient(ellipse at 50% 40%,#1d2246 0%,#131634 70%)}
.contact h2{position:absolute;left:111px;top:60px;font-family:'Poppins',sans-serif;font-size:46px;line-height:58px;font-weight:700;color:#fff}
.contact .rule{position:absolute;left:112px;top:190px;width:116px;height:4px;background:var(--green)}
.clabel{position:absolute;font-family:'Poppins',sans-serif;font-size:17px;font-weight:600;color:#fff}
.cval{position:absolute;font-size:16px;line-height:25px;color:var(--green);font-family:'Poppins',sans-serif}
.field{position:absolute;left:679px;width:409px;border:1.5px solid #c9cbd6;color:#fff;font-size:14px;font-weight:500;padding:0 22px;display:flex;align-items:center}
.submit{position:absolute;left:957px;top:426px;width:131px;height:44px;background:var(--green);color:#fff;font-family:'Poppins',sans-serif;font-weight:600;font-size:18px;display:flex;align-items:center;justify-content:center}
.copy{position:absolute;left:0;top:488px;width:1200px;text-align:center;color:#fff;font-size:14.5px}
</style>
</head>
<body>

<header class="hero">
  <div class="hero-photo" role="img" aria-label="Photo of three colleagues gathered around a laptop in a bright office"></div>
  <div class="brand" style="left:113px;top:34px;font-size:17px"><span class="dot"></span>CREWLINE</div>
  <nav class="nav">
    <span class="active">HOME</span><span class="sep">/</span>
    <span>ABOUT</span><span class="sep">/</span>
    <span>OUR SERVICES</span><span class="sep">/</span>
    <span>USER STORIES</span><span class="sep">/</span>
    <span>ONSHORE | OFFSHORE</span><span class="sep">/</span>
    <span>CONTACT US</span>
  </nav>
  <h1 class="hero-title">
    <span class="big">CREWLINE</span>
    <span class="line" style="margin-top:4px">RECRUITMENT PROCESS</span>
    <span class="line">OUTSOURCING <span class="g">WITH</span></span>
    <span class="line g">GROWTH AMBITIONS</span>
  </h1>
  <div class="btn btn-green" style="left:115px;top:428px;width:150px;height:42px;font-size:15px">GET STARTED</div>
  <span class="hero-arrow" style="left:57px"></span>
  <span class="hero-arrow" style="left:1109px;border-color:rgba(255,255,255,.8)"></span>
  <div class="dots"><i></i><i class="on"></i><i></i><i></i></div>
</header>

<section class="services">
  <h2 class="sec-title" style="top:76px;font-size:38px">OUR SERVICES</h2>
  <p class="sec-sub" style="top:128px">Lorem ipsum dolor sit amet, consectetur adipiscing elit, sed do eiusmod tempor incididunt ut labore et dolore magna aliqua. Quis ipsum suspendisse ultrices gravida.</p>

  <svg class="chev" style="left:66px" width="16" height="28" viewBox="0 0 16 28"><path d="M14 2L3 14l11 12" fill="none" stroke="#333" stroke-width="2"/></svg>
  <svg class="chev" style="left:1116px" width="16" height="28" viewBox="0 0 16 28"><path d="M2 2l11 12L2 26" fill="none" stroke="#333" stroke-width="2"/></svg>

  <div class="svc" style="left:90px">
    <svg width="68" height="68" viewBox="0 0 68 68"><circle cx="34" cy="34" r="31" fill="none" stroke="#121330" stroke-width="4"/><ellipse cx="34" cy="34" rx="13" ry="31" fill="none" stroke="#121330" stroke-width="3"/><path d="M4 34h60M9 18h50M9 50h50" stroke="#121330" stroke-width="3"/></svg>
    <h3>OUTSOURCING</h3>
    <p>Lorem ipsum dolor sit met, consectur adipiscing elit, sed do eiusmod tempor incididunt ut labore et dolore magna aliqua. Quis ipsum suspendisse ultrices gravida. Risus commodo</p>
  </div>
  <div class="divider" style="left:429px"></div>
  <div class="svc" style="left:431px">
    <svg width="68" height="68" viewBox="0 0 68 68"><circle cx="34" cy="26" r="9" fill="#0be597"/><path d="M18 56c0-10 7-17 16-17s16 7 16 17z" fill="#0be597"/><circle cx="12" cy="14" r="6" fill="#0be597"/><circle cx="56" cy="14" r="6" fill="#0be597"/><circle cx="12" cy="54" r="6" fill="#0be597"/><circle cx="56" cy="54" r="6" fill="#0be597"/></svg>
    <h3>ONSHORE</h3>
    <p>Lorem ipsum dolor sit met, consectur adipiscing elit, sed do eiusmod tempor incididunt ut labore et dolore magna aliqua. Quis ipsum suspendisse ultrices gravida. Risus commodo</p>
  </div>
  <div class="divider" style="left:769px"></div>
  <div class="svc" style="left:771px">
    <svg width="68" height="68" viewBox="0 0 68 68"><path d="M4 22h12v24H4zM52 22h12v24H52z" fill="#121330"/><path d="M16 26l14-6 8 4 14-4v24l-12 8-10-6-14-2z" fill="#121330"/></svg>
    <h3>OFFSHORE</h3>
    <p>Lorem ipsum dolor sit met, consectur adipiscing elit, sed do eiusmod tempor incididunt ut labore et dolore magna aliqua. Quis ipsum suspendisse ultrices gravida. Risus commodo</p>
  </div>

  <div class="btn btn-dark" style="left:179px;top:455px;width:162px;height:40px">VIEW MORE</div>
  <div class="btn btn-green" style="left:520px;top:455px;width:162px;height:40px">VIEW MORE</div>
  <div class="btn btn-dark" style="left:860px;top:455px;width:162px;height:40px">VIEW MORE</div>
</section>

<section class="newsletter">
  <h2>SUBSCRIBE TO NEWSLETTER</h2>
  <div class="email">Your Email
    <div class="email-btn"><svg style="position:absolute;left:22px;top:15px" width="26" height="26" viewBox="0 0 26 26"><path d="M24 2L2 12l8 3 2 9 4-6 6 4z" fill="#fff"/></svg></div>
  </div>
</section>

<section class="value">
  <div class="value-photo" role="img" aria-label="Overhead photo of a team working around a round meeting table with a tablet and papers"></div>
  <h2>OUR VALUE</h2>
  <p class="lead">Lorem ipsum dolor sit amet, consectetur adipiscing elit, sed do eiusmod tempor incididunt</p>
  <div class="vbox dark">
    <h3>SEED AND EARLY STAGE COMPANIES</h3>
    <p>Lorem ipsum dolor sit amet, consectetur adipiscing elit, sed do eiusmod incididunt ut labore et dolore magna ua. Quis ipsum suspendisse ultrices gravida.</p>
  </div>
  <div class="vbox bright">
    <h3>GROWTH AND LATE STAGE COMPANIES</h3>
    <p>Lorem ipsum dolor sit amet, consectetur adipiscing elit, sed do eiusmod incididunt ut labore et dolore magna ua. Quis ipsum suspendisse ultrices gravida.</p>
  </div>
</section>

<section class="stories">
  <h2 class="sec-title" style="top:76px;font-size:42px;color:#fff">USER STORIES</h2>
  <p class="sec-sub" style="top:128px;color:#fff">Lorem ipsum dolor sit amet, consectetur adipiscing elit, sed do eiusmod tempor incididunt ut labore et dolore magna aliqua. Quis ipsum suspendisse ultrices gravida.</p>

  <div class="card" style="left:116px">
    <div class="stars"><svg width="86" height="16" viewBox="0 0 86 16"><g fill="#f4a821"><path id="st" d="M8 0l2.4 5 5.6.6-4.2 3.8 1.2 5.6L8 12.2 3 15l1.2-5.6L0 5.6 5.6 5z"/><use href="#st" x="17"/><use href="#st" x="34"/><use href="#st" x="51"/><use href="#st" x="68"/></g></svg></div>
    <span class="badge"></span>
    <p>Lorem ictetur adipiscing elit, sed do eiusmod tempor incididunt ut labore et dolore magna aliqua. Quis ipsum suspendisse ultrices gravida.</p>
    <div class="who">- John Doe</div>
  </div>
  <div class="card" style="left:454px">
    <div class="stars"><svg width="86" height="16" viewBox="0 0 86 16"><g fill="#f4a821"><use href="#st"/><use href="#st" x="17"/><use href="#st" x="34"/><use href="#st" x="51"/><use href="#st" x="68"/></g></svg></div>
    <span class="badge"></span>
    <p>Lorem ictetur adipiscing elit, sed do eiusmod tempor incididunt ut labore et dolore magna aliqua. Quis ipsum suspendisse ultrices gravida.</p>
    <div class="who">- John Doe</div>
  </div>
  <div class="card" style="left:790px">
    <div class="stars"><svg width="86" height="16" viewBox="0 0 86 16"><g fill="#f4a821"><use href="#st"/><use href="#st" x="17"/><use href="#st" x="34"/><use href="#st" x="51"/><use href="#st" x="68"/></g></svg></div>
    <span class="badge"></span>
    <p>Lorem ictetur adipiscing elit, sed do eiusmod tempor incididunt ut labore et dolore magna aliqua. Quis ipsum suspendisse ultrices gravida.</p>
    <div class="who">- John Doe</div>
  </div>
</section>

<section class="leader">
  <div class="avatar" role="img" aria-label="Portrait photo of the managing director"></div>
  <div class="name">DANIEL <span>REYES</span></div>
  <div class="role">MANAGING DIRECTOR | CHIEF PERSPECTIVE</div>
  <p class="bio">Lorem ipsum dolor sit amet, consectetur adipiscsceo eiusmod tempor incididunt ut labore et dolore magna aliqua. ipsum spendisse ultrices gravida. Risus commodo viverra maecenus vel facilisis. Lorem ipsum dolor sit amet, consectetur adipiscing elit, sed do tempor iididunt ut labore et dolore magna aliqua. Quis ipsus a. Risus commodo viverra maecenas accumsan lacus vel facilisis. Lorem ipsum dolor sit amet, consectetur adipiscsceo eiusmod</p>
  <div class="socials" style="left:111px;top:450px"><i style="width:36px;height:36px"></i><i style="width:36px;height:36px"></i><i style="width:36px;height:36px"></i><i style="width:36px;height:36px"></i></div>
  <div class="vline"></div>

  <div class="stat" style="top:103px">10+</div>
  <div class="stat-t" style="top:114px">year’s Experience</div>
  <p class="stat-p" style="top:149px">Lorem ipsum dolor sit amet, consectetur ing elit, sed do eiusmod tempor incididunt ut</p>

  <div class="stat" style="top:241px">200+</div>
  <div class="stat-t" style="top:252px">Public &amp; Private Companies</div>
  <p class="stat-p" style="top:287px">Lorem ipsum dolor sit amet, consectetur ing elit, sed do eiusmod tempor incididunt ut</p>

  <div class="stat" style="top:377px">100%</div>
  <div class="stat-t" style="top:388px">Satisfaction</div>
  <p class="stat-p" style="top:423px">Lorem ipsum dolor sit amet, consectetur ing elit, sed do eiusmod tempor incididunt ut</p>
</section>

<section class="news">
  <h2 class="sec-title" style="top:72px;font-size:38px">NEWS AND INSIGHTS</h2>
  <article class="ncard" style="left:112px">
    <div class="nimg" role="img" aria-label="Photo of colleagues in a meeting around a table" style="background:linear-gradient(135deg,#8d8f92,#d9d6d2 60%,#6f7479)"></div>
    <h4>LOREM IPSUM DOLOR SITAMET, CONSECTETUR ADIPISCING</h4>
    <p>Lorem ipsum dolor sit amet, ctetur adipiscing elit, sed do eiusmod tempor incit ut labore et dolore magna aliqua.</p>
    <div class="more">CONTINUE READING</div>
  </article>
  <article class="ncard" style="left:444px">
    <div class="nimg" role="img" aria-label="Photo of hands pointing at business charts on a desk" style="background:linear-gradient(135deg,#5d6065,#c7c9cc 55%,#e9eaeb)"></div>
    <h4>LOREM IPSUM DOLOR SITAMET, CONSECTETUR ADIPISCING</h4>
    <p>Lorem ipsum dolor sit amet, ctetur adipiscing elit, sed do eiusmod tempor incit ut labore et dolore magna aliqua.</p>
    <div class="more">CONTINUE READING</div>
  </article>
  <article class="ncard" style="left:777px">
    <div class="nimg" role="img" aria-label="Photo of a young team laughing around laptops" style="background:linear-gradient(135deg,#7a6b5c,#b7a894 55%,#5d5a58)"></div>
    <h4>LOREM IPSUM DOLOR SITAMET, CONSECTETUR ADIPISCING</h4>
    <p>Lorem ipsum dolor sit amet, ctetur adipiscing elit, sed do eiusmod tempor incit ut labore et dolore magna aliqua.</p>
    <div class="more">CONTINUE READING</div>
  </article>
</section>

<footer class="contact">
  <h2>GET IN TOUCH<br>WITH US</h2>
  <div class="rule"></div>
  <div class="brand" style="left:113px;top:253px;font-size:14px;color:#fff"><span class="dot" style="background:#fff;width:11px;height:11px"></span>CREWLINE</div>

  <div class="clabel" style="left:356px;top:235px">TELEPHONE</div>
  <div class="cval" style="left:356px;top:260px">+888 888 8888</div>
  <div class="clabel" style="left:112px;top:313px">DIRECT MESSAGE</div>
  <div class="cval" style="left:112px;top:338px;width:210px">City name 10150, United States</div>
  <div class="clabel" style="left:356px;top:313px">DIRECT MESSAGE</div>
  <div class="cval" style="left:356px;top:338px">info@crewline.example</div>
  <div class="socials" style="left:112px;top:400px;gap:10px"><i style="width:44px;height:44px"></i><i style="width:44px;height:44px"></i><i style="width:44px;height:44px"></i><i style="width:44px;height:44px"></i></div>

  <div class="field" style="top:80px;height:57px">FULL NAME</div>
  <div class="field" style="top:149px;height:57px">EMAIL</div>
  <div class="field" style="top:218px;height:56px">SUBJECT</div>
  <div class="field" style="top:287px;height:127px;align-items:flex-start;padding-top:22px">HOW CAN WE HELP YOU</div>
  <div class="submit">SUBMIT</div>
  <div class="copy">Crewline &nbsp;© 2020 All Rights Reserved | Privacy Policy</div>
</footer>

</body>
</html>
```